Cafe menu flyer design

I need if possible A4 double sided menus. Two exemplars: first will contain breakfast menu on one side & refreshments menu on the other side, second exemplar will contain lunch menu on one side & refreshments menu on the other side. We do not need a description of the cafe or any history on these flyers, but design should reflect our surroundings and activities this area. We are located in main ski resort in UK-Cairngorm Mountains, right on the main ski road. The slopes are only 2 miles away from us. We are also very popular with wild life enthusiasts. Continues in design brief!

```html
<!DOCTYPE html>
<html lang="en">
<head>
<meta charset="utf-8">
<title>Morag's @ Ardven Cafe – Lunch Menu</title>
<link rel="stylesheet" href="https://fonts.googleapis.com/css2?family=Jost:wght@500;600&family=Playfair+Display:ital,wght@1,900&display=swap">
<style>
  :root {
    --navy: #1d1b3b;
    --sky: #8fd0ee;
    --mountain: #857a97;
    --forest: #7aab1f;
    --ink: #0b0b12;
    --cream: #ffffff;
    --robin: #d8232a;
  }
  html, body { margin: 0; padding: 0; overflow: hidden; background: var(--navy); }
  .flyer {
    position: relative;
    width: 1200px;
    height: 927px;
    overflow: hidden;
    background: var(--navy);
    color: var(--cream);
    font-family: "Jost", "Futura", sans-serif;
    font-weight: 600;
  }
  .scene {
    position: absolute; left: 0; top: 0; width: 1200px; height: 318px;
    background: linear-gradient(to bottom,
      var(--sky) 0%, var(--sky) 8%,
      var(--mountain) 24%, var(--mountain) 72%,
      var(--forest) 80%, var(--forest) 96%,
      var(--navy) 100%);
  }
  .masthead { position: absolute; left: 74px; top: 92px; width: 1040px; }
  .cafe-name {
    margin: 0;
    font-family: "Playfair Display", "Bodoni Moda", serif;
    font-style: italic; font-weight: 900;
    font-size: 82px; line-height: 1;
    color: var(--ink);
    letter-spacing: -1px;
  }
  .cafe-contact {
    position: absolute; left: 468px; top: 90px;
    font-size: 15.5px; color: var(--ink); white-space: nowrap;
  }
  .menu-title {
    position: absolute; left: 60px; top: 320px; margin: 0;
    font-size: 25px; font-weight: 600; letter-spacing: 0.5px;
  }
  .menu-col {
    position: absolute; top: 360px;
    list-style: none; margin: 0; padding: 0;
    font-size: 19.5px; line-height: 27.4px;
  }
  .menu-col--left { left: 71px; width: 498px; }
  .menu-col--right { left: 612px; width: 497px; }
  .item { display: flex; justify-content: space-between; white-space: nowrap; }
  .item--indent { padding-left: 248px; }
  .item--indent .label { flex: 1; }
  .note { font-style: italic; font-weight: 500; }
  .bird {
    position: absolute; left: 37px; top: 758px; width: 220px; height: 169px;
    background: var(--robin); border-radius: 60px 90px 0 0;
  }
  .footnote {
    position: absolute; left: 264px; top: 775px; margin: 0;
    font-size: 19px; line-height: 27px; width: 420px;
  }
  .social-mark {
    position: absolute; left: 733px; top: 770px; width: 100px; height: 100px;
    background: var(--cream); border-radius: 14px;
  }
  .social {
    position: absolute; left: 850px; top: 772px; width: 290px; margin: 0;
    text-align: center; font-size: 19.5px; line-height: 27px;
  }
</style>
</head>
<body>
<main class="flyer">
  <div class="scene" role="img" aria-label="Illustration of snowy purple mountains under a blue sky with clouds, a skier on the slope and a row of green pine trees"></div>

  <header class="masthead">
    <h1 class="cafe-name">Morag's @ Ardven Cafe</h1>
    <p class="cafe-contact">Ardven, Strathbeg, PH40 9XZ. &nbsp;Tel:01555010482</p>
  </header>

  <h2 class="menu-title">LUNCH MENU 12-4PM</h2>

  <ul class="menu-col menu-col--left">
    <li class="item"><span>Soup of the day</span><span>£3.75</span></li>
    <li class="note">served with brown roll &amp; butter</li>
    <li class="item"><span>Freshly made toasties: one filling</span><span>£3.20</span></li>
    <li class="item item--indent"><span class="label">two fillings</span><span>£4.20</span></li>
    <li>Sundried tomato,pesto and Mozzarella cheese</li>
    <li>Mozzarella and salami</li>
    <li>Cheese and ham</li>
    <li>Cheese and onion</li>
    <li>Cheese and tomato</li>
    <li>!Paninis with fillings as above coming soon!</li>
    <li class="item item--indent"><span class="label">One filling</span><span>£4.20</span></li>
    <li class="item item--indent"><span class="label">Two filling</span><span>£5.20</span></li>
    <li class="item"><span>Local butchers beef burger meal</span><span>£7.95</span></li>
    <li class="note">served with chips and salad</li>
  </ul>

  <ul class="menu-col menu-col--right">
    <li class="item"><span>Home made chicken fillet burger meal</span><span>£7.95</span></li>
    <li class="note">served with chips and salad</li>
    <li class="item"><span>Burger in a bun(on its own)</span><span>£4.20</span></li>
    <li class="item"><span>Pies assorted</span><span>£2.50</span></li>
    <li class="item"><span>Pie with beans</span><span>£3.50</span></li>
    <li class="item"><span>Pie with chips</span><span>£5.00</span></li>
    <li class="item"><span>Pie with beans and chips</span><span>£6.00</span></li>
    <li class="item"><span>Basket of chips</span><span>£3.50</span></li>
    <li class="item"><span>Chip butty</span><span>£2.00</span></li>
    <li class="item"><span>Chips &amp; beans</span><span>£4.50</span></li>
    <li class="item"><span>Chips &amp; cheese</span><span>£4.50</span></li>
    <li class="item"><span>Rolls with assorted</span><span>£2.20 - £3.20</span></li>
    <li>cold fillings</li>
  </ul>

  <div class="bird" role="img" aria-label="Illustration of a red bird standing on thin legs"></div>

  <p class="footnote">Gluten free bread and cakes available - ask staff!<br>At the height of the season evening meals available. Ask staff for more info.</p>

  <div class="social-mark" aria-hidden="true"></div>
  <p class="social">Like us on Chatterbook!<br>chatterbook.com/pages/<br>Morags-at-Ardven-<br>Cafe/500100200300400</p>
</main>
</body>
</html>
```